Night Dresses business cards business requirers

We are a new company initiating Mexico operations. Our core business is Night woman dress (both formal and party dress) for rent. Gownvella is the name of the company. ITS Gownvella form by two word. The dress word and topia (Utopic) so the place Gownvella Means That You cant get the ideal, perfect and unique dress for your event. So we would like a modern, very creative, and attractive business card.

Industry/Entity Type

Womens Clothing

Contact Information for Business Card

Rounded Borders, two faces

Requirements
Must have
• Rounded borders, logo and slogan, modern, glam, attractive design
Should not have
• modern design classic or not

```html
<!DOCTYPE html>
<html lang="en">
<head>
<meta charset="utf-8">
<title>Gownvella Business Card</title>
<link rel="stylesheet" href="https://fonts.googleapis.com/css2?family=Open+Sans:wght@400;600&display=swap">
<style>
  :root {
    --backdrop: #8c8c8c;
    --paper: #e8e8e8;
    --ink-deep: #262626;
    --ink-dark: #2e2e2e;
    --ink-mid: #3c3c3c;
    --ink-soft: #474747;
    --rose: #b8639a;
    --rose-light: #d472ae;
    --text-grey: #555555;
    --white: #ffffff;
  }
  html, body {
    margin: 0;
    padding: 0;
    width: 980px;
    height: 1200px;
    overflow: hidden;
    background: var(--backdrop);
  }
  .canvas {
    display: block;
    width: 980px;
    height: 1200px;
  }
  .strip-deep { fill: var(--ink-deep); }
  .strip-dark { fill: var(--ink-dark); }
  .strip-mid { fill: var(--ink-mid); }
  .strip-soft { fill: var(--ink-soft); }
  .paper { fill: var(--paper); }
  .ribbon { fill: var(--rose); }
  .ribbon-fold { fill: var(--rose-light); }
  .tag-window { fill: var(--paper); }
  .brand-dot { fill: var(--rose); }
  .brand-name {
    font-family: "Open Sans", sans-serif;
    font-weight: 600;
    fill: var(--text-grey);
  }
  .brand-slogan {
    font-family: "Open Sans", sans-serif;
    font-weight: 400;
    fill: var(--text-grey);
  }
  .contact-icon-bg { fill: var(--ink-soft); }
  .contact-icon { fill: var(--rose-light); }
  .contact-icon-line { fill: none; stroke: var(--rose-light); stroke-width: 1.4; }
  .contact-strong {
    font-family: "Open Sans", sans-serif;
    font-weight: 600;
    fill: var(--white);
  }
  .contact-plain {
    font-family: "Open Sans", sans-serif;
    font-weight: 400;
    fill: var(--white);
  }
</style>
</head>
<body>
<svg class="canvas" viewBox="0 0 885 1084" xmlns="http://www.w3.org/2000/svg" aria-label="Gownvella business card, front and back">

  <g class="card card-front">
    <rect class="strip-dark" x="114" y="117" width="62" height="373"/>
    <rect class="strip-mid" x="175" y="117" width="41" height="373"/>
    <rect class="paper" x="215" y="117" width="445" height="373"/>
    <rect class="strip-soft" x="659" y="117" width="39" height="373"/>
    <rect class="strip-deep" x="697" y="117" width="60" height="373"/>

    <g class="ribbon-set">
      <rect class="ribbon" x="114" y="160" width="62" height="40"/>
      <polygon class="ribbon-fold" points="175,160 224,170 224,210 175,200"/>
      <rect class="ribbon" x="114" y="245" width="62" height="40"/>
      <polygon class="ribbon-fold" points="175,245 224,255 224,295 175,285"/>
      <rect class="ribbon" x="114" y="328" width="62" height="40"/>
      <polygon class="ribbon-fold" points="175,328 224,338 224,378 175,368"/>
      <rect class="ribbon" x="114" y="406" width="62" height="40"/>
      <polygon class="ribbon-fold" points="175,406 224,416 224,456 175,446"/>
    </g>

    <g class="name-tag">
      <polygon class="ribbon" points="643,262 659,248 659,345 643,331"/>
      <rect class="ribbon-fold" x="659" y="264" width="83" height="81"/>
      <rect class="tag-window" x="666" y="280" width="65" height="49"/>
    </g>

    <g class="brand">
      <circle class="brand-dot" cx="282" cy="300" r="14"/>
      <text class="brand-name" x="308" y="304" font-size="30">Gownvella</text>
      <text class="brand-slogan" x="310" y="328" font-size="14">Evening wear to hire</text>
    </g>
  </g>

  <g class="card card-back">
    <rect class="strip-dark" x="106" y="641" width="33" height="372"/>
    <rect class="strip-mid" x="138" y="641" width="23" height="372"/>
    <rect class="paper" x="160" y="641" width="271" height="372"/>
    <rect class="strip-soft" x="430" y="641" width="53" height="372"/>
    <rect class="strip-mid" x="482" y="641" width="271" height="372"/>

    <g class="ribbon-set">
      <rect class="ribbon" x="106" y="688" width="33" height="40"/>
      <polygon class="ribbon-fold" points="138,688 165,698 165,738 138,728"/>
      <rect class="ribbon" x="106" y="768" width="33" height="40"/>
      <polygon class="ribbon-fold" points="138,768 165,778 165,818 138,808"/>
      <rect class="ribbon" x="106" y="850" width="33" height="40"/>
      <polygon class="ribbon-fold" points="138,850 165,860 165,900 138,890"/>
      <rect class="ribbon" x="106" y="929" width="33" height="40"/>
      <polygon class="ribbon-fold" points="138,929 165,939 165,979 138,969"/>
    </g>

    <g class="brand">
      <circle class="brand-dot" cx="295" cy="810" r="14"/>
      <text class="brand-name" x="295" y="868" font-size="30" text-anchor="middle">Gownvella</text>
      <text class="brand-slogan" x="295" y="891" font-size="14" text-anchor="middle">Evening wear to hire</text>
    </g>

    <g class="contact-list">
      <g class="contact-row contact-name">
        <rect class="ribbon" x="482" y="670" width="271" height="43"/>
        <polygon class="ribbon-fold" points="420,684 482,670 482,713 430,726 420,718"/>
        <circle class="contact-icon-bg" cx="459" cy="697" r="15"/>
        <circle class="contact-icon" cx="459" cy="692" r="4.5"/>
        <path class="contact-icon" d="M451,705 a8,7 0 0 1 16,0 z"/>
        <text class="contact-strong" x="614" y="688" font-size="19" text-anchor="middle">Individual Name</text>
        <text class="contact-plain" x="614" y="708" font-size="14" text-anchor="middle">Position</text>
      </g>
      <g class="contact-row contact-phone">
        <rect class="ribbon" x="482" y="757" width="271" height="43"/>
        <polygon class="ribbon-fold" points="420,771 482,757 482,800 430,813 420,805"/>
        <circle class="contact-icon-bg" cx="459" cy="784" r="15"/>
        <path class="contact-icon" d="M452,775 l4,-2 3,6 -3,2 q2,5 6,8 l2,-3 6,3 -2,4 q-9,1 -16,-18 z"/>
        <text class="contact-strong" x="612" y="781" font-size="19" text-anchor="middle">phone number</text>
      </g>
      <g class="contact-row contact-email">
        <rect class="ribbon" x="482" y="844" width="271" height="43"/>
        <polygon class="ribbon-fold" points="420,858 482,844 482,887 430,900 420,892"/>
        <circle class="contact-icon-bg" cx="460" cy="870" r="15"/>
        <g class="contact-icon-line">
          <circle cx="460" cy="870" r="11"/>
          <ellipse cx="460" cy="870" rx="5" ry="11"/>
          <line x1="449" y1="870" x2="471" y2="870"/>
          <line x1="451" y1="864" x2="469" y2="864"/>
          <line x1="451" y1="876" x2="469" y2="876"/>
        </g>
        <text class="contact-plain" x="618" y="870" font-size="17" text-anchor="middle">E-mail</text>
      </g>
      <g class="contact-row contact-web">
        <rect class="ribbon" x="482" y="933" width="271" height="43"/>
        <polygon class="ribbon-fold" points="420,947 482,933 482,976 430,989 420,981"/>
        <circle class="contact-icon-bg" cx="460" cy="958" r="15"/>
        <g class="contact-icon-line">
          <circle cx="460" cy="958" r="11"/>
          <ellipse cx="460" cy="958" rx="5" ry="11"/>
          <line x1="449" y1="958" x2="471" y2="958"/>
          <line x1="451" y1="952" x2="469" y2="952"/>
          <line x1="451" y1="964" x2="469" y2="964"/>
        </g>
        <text class="contact-plain" x="618" y="959" font-size="17" text-anchor="middle">Website</text>
      </g>
    </g>
  </g>
</svg>
</body>
</html>
```